Book Cover for Productivity Book

I need a book cover for my latest publication "On Momentum: The Gathered Insights of the Busiest Woman Living"

You can see my branding at www.brightmarrow.example

This is meant to be my epic pinaccle work on productivity, I want it to look like the end all be all word on productivity.

Target Market(s)

entrepreneurs

```html
<!DOCTYPE html>
<html lang="en">
<head>
<meta charset="utf-8">
<title>On Momentum — Book Cover</title>
<link rel="stylesheet" href="https://fonts.googleapis.com/css2?family=Josefin+Sans:ital,wght@0,100;0,200;0,700;1,300;1,400&display=swap">
<style>
  :root {
    --page-bg: #f4f4f4;
    --cover-red: #a51c23;
    --cover-red-deep: #8e111a;
    --cover-red-edge: #5f0a0f;
    --emblem-red: #7d0c14;
    --title-white: #e8e8e8;
    --soft-white: #f3e6e6;
    --author-black: #121212;
  }
  html, body {
    margin: 0;
    width: 1200px;
    height: 1200px;
    overflow: hidden;
    background: var(--page-bg);
  }
  .canvas {
    position: relative;
    width: 1200px;
    height: 1200px;
  }
  .book-cover {
    position: absolute;
    left: 242px;
    top: 50px;
    width: 715px;
    height: 1100px;
    box-shadow: 0 10px 30px rgba(0,0,0,0.18);
  }
  .book-cover svg { display: block; }
  .tagline {
    font-family: 'Josefin Sans', sans-serif;
    font-style: italic;
    font-weight: 300;
    font-size: 25px;
    letter-spacing: 2px;
    fill: var(--soft-white);
  }
  .title-lead {
    font-family: 'Josefin Sans', sans-serif;
    font-weight: 700;
    font-size: 330px;
    fill: var(--title-white);
  }
  .title-word {
    font-family: 'Josefin Sans', sans-serif;
    font-weight: 100;
    font-size: 86px;
    fill: var(--title-white);
  }
  .subtitle {
    font-family: 'Josefin Sans', sans-serif;
    font-style: italic;
    font-weight: 400;
    font-size: 24px;
    letter-spacing: 2px;
    fill: var(--soft-white);
  }
  .author {
    font-family: 'Josefin Sans', sans-serif;
    font-size: 76px;
    fill: var(--author-black);
  }
  .author-first { font-weight: 200; }
  .author-last { font-weight: 700; }
  .emblem-area { fill: var(--emblem-red); opacity: 0.55; }
</style>
</head>
<body>
<div class="canvas">
  <div class="book-cover">
    <svg width="715" height="1100" viewBox="0 0 715 1100" xmlns="http://www.w3.org/2000/svg">
      <defs>
        <linearGradient id="coverShade" x1="0" y1="0" x2="1" y2="0">
          <stop offset="0" stop-color="#a51c23"/>
          <stop offset="0.6" stop-color="#8e111a"/>
          <stop offset="1" stop-color="#5f0a0f"/>
        </linearGradient>
      </defs>
      <rect class="cover-base" width="715" height="1100" fill="url(#coverShade)"/>

      <text class="tagline" x="357" y="115" text-anchor="middle">The epic pinaccle work on productivity</text>

      <text class="title-lead" x="357" y="478" text-anchor="middle">ON</text>

      <text class="title-word" x="357" y="588" text-anchor="middle" textLength="545" lengthAdjust="spacingAndGlyphs">MOMENTUM</text>

      <rect class="emblem-area" x="272" y="672" width="146" height="74" rx="8" role="img" aria-label="Small hand-drawn emblem: less equals more"/>

      <text class="subtitle" x="357" y="850" text-anchor="middle">The Gathered Insights of the</text>
      <text class="subtitle" x="357" y="881" text-anchor="middle">Busiest Woman Living</text>

      <text class="author" x="357" y="1025" text-anchor="middle"><tspan class="author-first">MIRA </tspan><tspan class="author-last">CASTELL</tspan></text>
    </svg>
  </div>
</div>
</body>
</html>
```